Kestrel Pass Partners Business Card

Boston based immigration and tax law firm.
Will serve wealthy individuals who wish to immigrate to the US.
Colors as in Logo, blue white.
Delivering sophisticated legal services.
Attached please see logo design from website.
Target Market(s)
non-US citizens
Industry/Entity Type
Legal
Contact Information for Business Card
Dennis R. Hargrove, Esq. LL.M, M.Sc., M.Fin
Kestrel Pass Partners LLC
47 Tallis Rd., #518
Boston, MA 02134
Boston +1 617 555 0192
London +44 20 7946 0583
Sydney +61 2 9876 5310
www.kestrelpasspartners.example
dhargrove@kestrelpasspartners.example
United States Immigration and Tax Counsel

```html
<!DOCTYPE html>
<html lang="en">
<head>
<meta charset="UTF-8">
<title>Kestrel Pass Partners — Business Card</title>
<link href="https://fonts.googleapis.com/css2?family=Marcellus&display=swap" rel="stylesheet">
<style>
  :root {
    --navy: #101a5e;
    --teal: #1c9fc8;
    --ink: #2a2f45;
    --paper: #ffffff;
    --backdrop: #ecebe9;
  }
  html, body {
    margin: 0;
    width: 1200px;
    height: 861px;
    overflow: hidden;
    background: var(--backdrop);
    font-family: "Marcellus", "Optima", serif;
  }
  .sheet {
    position: relative;
    width: 1200px;
    height: 861px;
  }
  .card {
    position: absolute;
    top: 290px;
    width: 500px;
    height: 286px;
    background: var(--paper);
    box-shadow: 0 2px 6px rgba(0,0,0,0.08), 0 12px 30px rgba(0,0,0,0.07);
    overflow: hidden;
  }
  .card--front { left: 70px; }
  .card--back { left: 630px; }

  /* Front */
  .corner {
    position: absolute;
    width: 44px;
    height: 44px;
  }
  .corner--navy { top: 0; left: 32px; background: var(--navy); }
  .corner--teal { bottom: 0; right: 22px; background: var(--teal); }

  .brand {
    position: absolute;
    top: 82px;
    left: 70px;
    display: flex;
    align-items: center;
    gap: 12px;
  }
  .brand__mark {
    width: 22px;
    height: 22px;
    border: 2px solid var(--teal);
    box-sizing: border-box;
  }
  .brand__name {
    font-size: 31px;
    color: var(--navy);
    letter-spacing: 0.3px;
  }
  .brand__rule {
    position: absolute;
    top: 130px;
    left: 70px;
    width: 360px;
    height: 2px;
    background: var(--navy);
  }
  .tagline {
    position: absolute;
    top: 148px;
    left: 70px;
    font-size: 14px;
    color: var(--ink);
    letter-spacing: 0.3px;
  }
  .website {
    position: absolute;
    top: 188px;
    left: 96px;
    font-size: 14px;
    color: var(--ink);
  }

  /* Back */
  .firm {
    position: absolute;
    top: 30px;
    left: 30px;
    display: flex;
    align-items: center;
    gap: 12px;
  }
  .firm__mark {
    width: 20px;
    height: 20px;
    border: 2px solid var(--teal);
    box-sizing: border-box;
  }
  .firm__name {
    font-size: 22px;
    color: var(--navy);
    letter-spacing: 0.4px;
  }
  .details {
    position: absolute;
    top: 96px;
    right: 30px;
    text-align: left;
    font-size: 13.5px;
    color: var(--ink);
    line-height: 30px;
    letter-spacing: 0.3px;
  }
  .phones {
    position: absolute;
    bottom: 30px;
    left: 30px;
    margin: 0;
    font-size: 13.5px;
    line-height: 20px;
    color: var(--ink);
    letter-spacing: 0.3px;
  }
  .phones__city { color: var(--teal); margin-right: 6px; }
</style>
</head>
<body>
<main class="sheet">
  <section class="card card--front" aria-label="Business card front">
    <div class="corner corner--navy"></div>
    <div class="brand">
      <span class="brand__mark"></span>
      <span class="brand__name">Kestrel Pass Partners</span>
    </div>
    <div class="brand__rule"></div>
    <p class="tagline" style="margin:0">United States Immigration and Tax Counsel</p>
    <p class="website" style="margin:0">www.kestrelpasspartners.example</p>
    <div class="corner corner--teal"></div>
  </section>

  <section class="card card--back" aria-label="Business card back">
    <div class="firm">
      <span class="firm__mark"></span>
      <span class="firm__name">Kestrel Pass Partners LLC</span>
    </div>
    <div class="details">
      <div class="details__address">47 Tallis Rd., #518 Boston, MA 02134</div>
      <div class="details__email">dhargrove@kestrelpasspartners.example</div>
    </div>
    <p class="phones">
      <span class="phones__city">Boston</span>+1 617 555 0192<br>
      <span class="phones__city">London</span>+44 20 7946 0583<br>
      <span class="phones__city">Sydney</span>+61 2 9876 5310
    </p>
  </section>
</main>
</body>
</html>
```